Accounting Practice Business Card Design

I have a logo I am happy for you to use in the design of the Business Card.
You can edit and change colours as you please, I am not fixated on it.
I am looking for a modern and clean overall feel for the finished design.

The business is a small accounting practice who thrives on word of mouth referrals and this card will be given to all current and prospect clients.

Industry/Entity Type

Accountant

Contact Information for Business Card

Marcus Elwin
Level 5, 8 Corvale Ridge Road
ASHGROVE RISE VIC 3187
Phone: 9481 3057
Email: melwin@mrfaccountants.com.au
Web: www.mrfaccountants.com.au

Font styles to use
Serif
Sans Serif

Colors
0555a3
3277b5
85acd3
0393ce
33a6d7
85cae6
00a990
33b8a4
9bcb3c

Requirements
Must have
• "The end to your tax problems begin with us"
• "A referral from you is our greatest compliment"
Nice to have
• Modern clean professional

```html
<!DOCTYPE html>
<html lang="en">
<head>
<meta charset="utf-8">
<title>MRF Accountants – Business Card</title>
<link rel="stylesheet" href="https://fonts.googleapis.com/css2?family=Saira:wdth,wght@50..125,300..700&display=swap">
<style>
  :root {
    --navy: #0555a3;
    --sky: #0393ce;
    --white: #ffffff;
    --navy-faint: #1261ad;
    --stage-light: #ddd8d8;
    --stage-dark: #717171;
  }
  * { margin: 0; padding: 0; box-sizing: border-box; }
  html, body { width: 1200px; height: 1000px; overflow: hidden; }
  body {
    position: relative;
    background: linear-gradient(90deg, var(--stage-light) 0%, #b3b0b0 45%, var(--stage-dark) 100%);
    font-family: "Saira", "Arial", sans-serif;
    font-stretch: 125%;
  }
  .card {
    position: absolute;
    left: 229px;
    width: 742px;
    height: 424px;
    overflow: hidden;
  }
  .card--front { top: 37px; background: var(--white); border: 1px solid #d6d6d6; }
  .card--back { top: 539px; background: var(--navy); }

  .front__tagline {
    position: absolute; top: 12px; left: 0; width: 100%;
    text-align: center; color: var(--sky);
    font-size: 21px; font-weight: 400; letter-spacing: 0.2px;
  }
  .contact {
    position: absolute; left: 8px; width: 374px; height: 74px;
    display: flex; align-items: center; color: var(--white);
  }
  .contact--dark { background: var(--navy); }
  .contact--light { background: var(--sky); }
  .contact__icon { width: 44px; height: 44px; margin-left: 18px; flex: none; fill: var(--white); }
  .contact__text { font-size: 17px; font-weight: 400; line-height: 1.05; margin-left: 4px; }
  .contact__text--phone { font-size: 25px; margin-left: 36px; letter-spacing: 1px; }
  .contact--phone { top: 55px; }
  .contact--email { top: 137px; }
  .contact--web { top: 220px; }
  .contact--address { top: 302px; }

  .front__name {
    position: absolute; top: 96px; left: 400px;
    color: var(--navy); font-size: 39px; font-weight: 400; white-space: nowrap;
  }
  .brand {
    position: absolute; text-align: center; font-weight: 700; line-height: 0.9;
  }
  .brand__short { display: block; }
  .brand--front { left: 408px; top: 168px; width: 300px; color: var(--sky); }
  .brand--front .brand__short { font-size: 104px; }
  .brand--front .brand__long { display: block; font-size: 27px; margin-top: 6px; }

  .back__watermark {
    position: absolute; left: 30px; top: 40px; width: 690px;
    color: var(--navy-faint); font-weight: 700; text-align: center; line-height: 0.9;
  }
  .back__watermark .brand__short { font-size: 230px; }
  .back__watermark .brand__long { display: block; font-size: 58px; }
  .brand--back { left: 150px; top: 100px; width: 442px; color: var(--white); }
  .brand--back .brand__short { font-size: 150px; }
  .brand--back .brand__long { display: block; font-size: 40px; margin-top: 10px; }
  .back__tagline {
    position: absolute; left: 0; width: 100%; top: 376px;
    text-align: center; color: var(--white); font-size: 24px; font-weight: 400;
  }
</style>
</head>
<body>
  <section class="card card--front">
    <p class="front__tagline">The end to your tax problems begin with us.</p>

    <div class="contact contact--dark contact--phone">
      <svg class="contact__icon" viewBox="0 0 24 24" aria-hidden="true"><path d="M6.6 10.8a15.1 15.1 0 0 0 6.6 6.6l2.2-2.2a1 1 0 0 1 1-.25 11.4 11.4 0 0 0 3.6.57 1 1 0 0 1 1 1V20a1 1 0 0 1-1 1A17 17 0 0 1 3 4a1 1 0 0 1 1-1h3.5a1 1 0 0 1 1 1c0 1.25.2 2.45.57 3.57a1 1 0 0 1-.25 1z"/></svg>
      <span class="contact__text contact__text--phone">9481 3057</span>
    </div>
    <div class="contact contact--light contact--email">
      <svg class="contact__icon" viewBox="0 0 24 24" aria-hidden="true"><path d="M2 5h20v14H2z M3.5 6.5v.3l8.5 6.2 8.5-6.2v-.3z M3.5 8.6v8.9h17V8.6L12 14.8z" fill-rule="evenodd"/></svg>
      <span class="contact__text">melwin@mrfaccountants.com.au</span>
    </div>
    <div class="contact contact--dark contact--web">
      <svg class="contact__icon" viewBox="0 0 24 24" aria-hidden="true" fill="none" stroke="#fff" stroke-width="1.4"><circle cx="12" cy="12" r="9.5"/><ellipse cx="12" cy="12" rx="4.2" ry="9.5"/><path d="M2.5 12h19M4 7h16M4 17h16M12 2.5v19"/></svg>
      <span class="contact__text">www.mrfaccountants.com.au</span>
    </div>
    <div class="contact contact--light contact--address">
      <svg class="contact__icon" viewBox="0 0 24 24" aria-hidden="true"><path d="M12 2 1 12h3v10h6v-6h4v6h6V12h3l-4-3.6V4h-2.5v2.2z"/></svg>
      <span class="contact__text">Level 5, 8 Corvale Ridge Road<br>ASHGROVE RISE VIC 3187</span>
    </div>

    <h1 class="front__name">Marcus Elwin</h1>
    <div class="brand brand--front">
      <span class="brand__short">MRF</span>
      <span class="brand__long">ACCOUNTANTS</span>
    </div>
  </section>

  <section class="card card--back">
    <div class="back__watermark" aria-hidden="true">
      <span class="brand__short">MRF</span>
      <span class="brand__long">ACCOUNTANTS</span>
    </div>
    <div class="brand brand--back">
      <span class="brand__short">MRF</span>
      <span class="brand__long">ACCOUNTANTS</span>
    </div>
    <p class="back__tagline">A referral from you is our greatest compliment.</p>
  </section>
</body>
</html>
```